Adventurous female pilot

I am looking for a personal business card, for a very well qualified female pilot, with a lot of aviation experience.

Currently an airline pilot, have worked as a bush pilot in Africa, looking to get into corporate aviation, or private jet owners.
Want a classy looking card for networking...

Could be interested in a retro\vintage look also?!

An idea,, is an african sunset background, with my wings\logo on it
Updates

I just want to say thank you to all of your for your amazing designs!

I have been very busy flying this past week , so not had a chance to be on the computer much.
But I provide some feedback, and conclusions very soon!
Thank you again.

Marla

Reason: Still waiting on a couple of revisions to be 100% about my choice!

Target Market(s)

corporate aviation, private jet owners, casino's,
General audience.
networking

Industry/Entity Type

Airline

Requirements
Nice to have
• Classy, edgy, sexy, but also feminine

```html
<!DOCTYPE html>
<html lang="en">
<head>
<meta charset="utf-8">
<title>Marla Hollis Aviation – Business Card</title>
<link rel="stylesheet" href="https://fonts.googleapis.com/css2?family=Questrial&display=swap">
<style>
  :root {
    --mint: #cfe3da;
    --mint-pale: #eef5f1;
    --white: #ffffff;
    --lavender: #ead6f6;
    --frame-line: #3a3a4a;
    --magenta: #c8177f;
    --teal-fill: #9ad8cf;
    --teal-ink: #1d4a4c;
    --ink: #454545;
    --silver-light: #e4e6e8;
    --silver-dark: #9a9fa4;
  }
  html, body {
    margin: 0;
    padding: 0;
    overflow: hidden;
    background: var(--white);
  }
  .card {
    position: relative;
    width: 1200px;
    height: 686px;
    overflow: hidden;
    background: linear-gradient(100deg, var(--mint) 0%, var(--mint-pale) 30%, var(--white) 55%, var(--white) 80%, var(--mint-pale) 100%);
    font-family: "Questrial", "Century Gothic", sans-serif;
  }
  .outer-frame {
    position: absolute;
    left: 87px;
    top: 85px;
    width: 1026px;
    height: 514px;
    box-sizing: border-box;
    background: var(--lavender);
    border: 1.5px solid var(--frame-line);
  }
  .inner-panel {
    position: absolute;
    left: 119px;
    top: 117px;
    width: 960px;
    height: 446px;
    box-sizing: border-box;
    background: var(--white);
    border: 2px solid var(--magenta);
    text-align: center;
  }
  .name {
    margin: 38px 0 0;
    font-size: 82px;
    font-weight: 400;
    letter-spacing: 1px;
    line-height: 1;
    color: var(--teal-fill);
    -webkit-text-stroke: 3px var(--teal-ink);
    paint-order: stroke fill;
  }
  .title {
    margin: 6px 0 0;
    font-size: 38px;
    line-height: 1;
    letter-spacing: 1px;
    color: var(--magenta);
  }
  .contacts {
    list-style: none;
    margin: 62px 0 0;
    padding: 0;
    font-size: 39px;
    line-height: 62px;
    color: var(--ink);
  }
  .wings-emblem {
    position: absolute;
    left: 361px;
    top: 562px;
    width: 485px;
    height: 124px;
    background: var(--white);
  }
  .wings-emblem .fill {
    position: absolute;
    inset: 8px 20px 0;
    border-radius: 50% 50% 40% 40% / 70% 70% 30% 30%;
    background: radial-gradient(ellipse at 50% 40%, var(--silver-light) 0%, var(--silver-dark) 100%);
  }
</style>
</head>
<body>
  <main class="card">
    <div class="outer-frame"></div>
    <section class="inner-panel">
      <h1 class="name">MARLA HOLLIS</h1>
      <p class="title">AVIATION</p>
      <ul class="contacts">
        <li>Cell US: +1 702-555-0143</li>
        <li>Cell Taipei: +886 970-555-214</li>
        <li>marlachollis@skymail.net</li>
      </ul>
    </section>
    <div class="wings-emblem" role="img" aria-label="Silver pilot wings insignia">
      <div class="fill"></div>
    </div>
  </main>
</body>
</html>
```